Want to incorporate elements of all these items to make an amazing sign to welcome people to the community. The sign is 6x4 and needs to incorporate the following items:

Welcome to Corwick Meadows

Come visit the PRD sales center at 745 thistledown road
High Speed Fiber Internet
Land financing starting at $299 (No credit checks)
Let us build your dream home!
555-284-7390
We like the gold and black design no teal or blue that was another agents design. Some combination of the current sign all the stuff listed above and then design elements that tie into the truck wrap.

Target Market(s)

People visiting the neighborhood

Industry/Entity Type

real estate and construction

Font styles to use
Serif

Colors

Designer to choose colors to be used in the design.

Requirements
Must have
• PRD Home Builders Welcomes you to Corwick Meadows, Let us build your dream home, Phone number, Land financing starting at $299 NO credit checks

```html
<!DOCTYPE html>
<html lang="en">
<head>
<meta charset="utf-8">
<title>Corwick Meadows – Welcome Sign</title>
<link rel="stylesheet" href="https://fonts.googleapis.com/css2?family=Poppins:wght@400;500;600&family=Homemade+Apple&display=swap">
<style>
  :root {
    --page-bg: #e9e7e3;
    --sign-white: #fbfbfa;
    --gold: #b49a76;
    --sand: #cdbba1;
    --ink: #1e1a19;
    --ink-soft: #8c8886;
    --tag-grey: #5b5755;
    --muted: #6b6764;
    --wood: #7a5a43;
    --foliage: #8a8a55;
  }
  * { box-sizing: border-box; margin: 0; padding: 0; }
  html, body {
    width: 1200px; height: 900px; overflow: hidden;
    background: var(--page-bg);
    font-family: "Poppins", sans-serif;
  }
  .sign {
    position: absolute; left: 50px; top: 98px;
    width: 1100px; height: 704px;
    background: var(--sign-white);
    box-shadow: 0 2px 10px rgba(0,0,0,.12);
    overflow: hidden;
  }
  .sign > * { position: absolute; }
  .welcome {
    right: 57px; top: 34px;
    font-size: 62px; font-weight: 500; letter-spacing: -0.5px;
    color: var(--gold); white-space: nowrap; line-height: 1.2;
  }
  .phone {
    right: 54px; top: 108px;
    font-size: 146px; font-weight: 500; letter-spacing: -4px;
    line-height: 1.1; white-space: nowrap;
    background: linear-gradient(90deg, var(--ink-soft), var(--ink) 70%);
    -webkit-background-clip: text; background-clip: text; color: transparent;
  }
  .home-render {
    left: 262px; top: 268px; width: 780px; height: 400px;
    border-radius: 40% 40% 8px 8px / 30% 30% 8px 8px;
    background:
      radial-gradient(ellipse at 25% 30%, rgba(138,138,85,.55), transparent 40%),
      radial-gradient(ellipse at 88% 25%, rgba(150,120,60,.55), transparent 35%),
      linear-gradient(160deg, #cfc8c0 0%, #9b6f52 45%, #4b4442 80%, #d9d6d2 100%);
  }
  .tag {
    left: 0; height: 24px;
    color: #fff; font-size: 14px; font-weight: 500;
    display: flex; align-items: center; justify-content: center;
    clip-path: polygon(4% 0, 100% 0, 96% 100%, 0 100%);
    background: var(--tag-grey);
  }
  .tag-financing { left: 63px; top: 303px; width: 253px; }
  .tag-internet  { left: 126px; top: 411px; width: 256px; }
  .price {
    left: 84px; top: 330px; width: 270px; height: 64px;
    clip-path: polygon(0 0, 88% 0, 100% 100%, 10% 100%);
    background: linear-gradient(90deg, var(--sand), #e1d4c0);
    color: #fff; font-size: 44px; font-weight: 500;
    display: flex; align-items: center; justify-content: center;
  }
  .tagline {
    left: 400px; top: 460px; width: 500px;
    font-family: "Homemade Apple", cursive;
    color: #fff; font-size: 40px; line-height: 1.6;
    transform: rotate(-9deg);
    text-shadow: 0 1px 3px rgba(0,0,0,.35);
  }
  .tagline span { display: block; }
  .tagline .line-two { margin-left: -50px; }
  .brand {
    left: 44px; top: 540px;
    font-size: 92px; font-weight: 500; letter-spacing: -2px;
    color: var(--sand); line-height: 1;
  }
  .sales-center {
    left: 44px; top: 663px;
    font-size: 13px; color: var(--muted);
  }
  .sales-center strong { font-weight: 500; color: var(--ink); }
  .fine-print {
    right: 54px; top: 666px;
    font-size: 11px; color: var(--muted);
  }
</style>
</head>
<body>
  <main class="sign">
    <h1 class="welcome">Welcome to Corwick Meadows</h1>
    <p class="phone">555-284-7390</p>

    <div class="home-render" role="img" aria-label="Rendering of a modern two-storey home with wood cladding, glass balcony, landscaped yard and trees"></div>

    <div class="tag tag-financing">Land financing starting at</div>
    <div class="price">$299</div>
    <div class="tag tag-internet">High Speed Fiber Internet</div>

    <p class="tagline"><span>Let us build</span><span class="line-two">your dream home!</span></p>

    <div class="brand">PRD</div>
    <p class="sales-center">Come visit the PRD sales center at : <strong>745 Thistledown Rd</strong></p>
    <p class="fine-print">*No credit checks</p>
  </main>
</body>
</html>
```